Crestline Decor Depot needs Business cards and letterhead

letterhead, envelope & business card
Letterhead:
Crestline Decor Depot
4823 Larkfield Drive Bozeman, MT 59744
Phone #: (406) 555-0148
Fax#: (406) 555-0192
Business cards:
Crestline Decor Depot
Phone #: (406) 555-0148
Fax#: (406) 555-0192
Corinne Vasko
corinne@crestlinedecordepot.example
www.crestlinedecordepot.example
Target Market(s)
Home Interiors client
Industry/Entity Type
Business
Requirements
Must have
- ONLY submit straight front view on white background
- I DO NOT WANT ANY MOCK UPS
Nice to have
- see attached logo use guide
Should not have

```html
<!DOCTYPE html>
<html lang="en">
<head>
<meta charset="utf-8">
<title>Crestline Decor Depot – Envelope</title>
<link href="https://fonts.googleapis.com/css2?family=Open+Sans:ital,wght@1,800&family=Questrial&display=swap" rel="stylesheet">
<style>
  :root {
    --sky: #5bb8e8;
    --brand-blue: #1273b9;
    --deep-blue: #1b68b3;
    --slate: #696969;
    --ink: #0d0d0d;
    --paper: #ffffff;
  }
  * { box-sizing: border-box; margin: 0; padding: 0; }
  html, body { width: 1107px; height: 1200px; overflow: hidden; background: var(--paper); }
  body { position: relative; font-family: "Questrial", sans-serif; }

  .side-label {
    position: absolute;
    font-family: "Open Sans", sans-serif;
    font-style: italic; font-weight: 800;
    font-size: 35px; letter-spacing: 4px; color: var(--ink);
  }
  .side-label--front { left: 171px; top: 50px; }
  .side-label--back { left: 107px; top: 616px; }

  .envelope {
    position: absolute; left: 44px; width: 1019px; height: 423px;
    background: var(--paper);
    box-shadow: 0 1px 4px rgba(0,0,0,.3);
    overflow: hidden;
  }
  .envelope--front { top: 128px; }
  .envelope--back { top: 722px; }

  .envelope__strip { position: absolute; left: 0; top: 0; width: 100%; height: 11px; background: var(--sky); }
  .envelope__tab { position: absolute; left: 0; top: 0; }

  .tab-contact { position: absolute; left: 640px; width: 379px; top: 22px; text-align: center; color: #fff; }
  .tab-contact__name { font-size: 20px; letter-spacing: .8px; text-transform: uppercase; padding-left: 30px; }
  .tab-contact__phones { font-size: 11px; letter-spacing: .4px; margin-top: 3px; padding-left: 14px; display: flex; justify-content: center; gap: 14px; }
  .tab-contact__phones span { display: inline-flex; align-items: center; gap: 6px; }

  .brand-name {
    position: absolute; display: flex; align-items: center;
    color: var(--slate); text-transform: uppercase; letter-spacing: .5px;
  }
  .brand-name__square { background: var(--brand-blue); flex: none; }
  .brand-name--small { left: 28px; top: 76px; font-size: 19px; gap: 8px; }
  .brand-name--small .brand-name__square { width: 10px; height: 10px; }
  .brand-name--large { left: 0; right: 0; justify-content: center; top: 268px; font-size: 30px; gap: 12px; }
  .brand-name--large .brand-name__square { width: 16px; height: 16px; }

  .footer-bar {
    position: absolute; left: 0; bottom: 0; width: 100%; height: 51px;
    background: var(--slate); color: #fff;
    display: flex; align-items: center; justify-content: center; gap: 20px;
    font-size: 12.5px; letter-spacing: .2px; text-transform: uppercase;
  }
  .footer-bar span { display: inline-flex; align-items: center; gap: 7px; }

  .envelope__flap { position: absolute; left: 0; top: 0; }
</style>
</head>
<body>
  <h2 class="side-label side-label--front">FRONT SIDE</h2>
  <section class="envelope envelope--front">
    <div class="envelope__strip"></div>
    <svg class="envelope__tab" width="1019" height="125" viewBox="0 0 1019 125">
      <polygon points="640,0 1019,0 1019,60 857,119 640,47" fill="var(--deep-blue)"/>
      <polygon points="640,0 1019,0 1019,55 857,107 640,47" fill="var(--sky)"/>
    </svg>
    <div class="tab-contact">
      <div class="tab-contact__name">Crestline Decor Depot</div>
      <div class="tab-contact__phones">
        <span><svg width="10" height="10" viewBox="0 0 24 24"><path fill="#fff" d="M6.6 10.8a15 15 0 0 0 6.6 6.6l2.2-2.2c.3-.3.7-.4 1-.2 1.1.4 2.3.6 3.6.6.6 0 1 .4 1 1V20c0 .6-.4 1-1 1A17 17 0 0 1 3 4c0-.6.4-1 1-1h3.5c.6 0 1 .4 1 1 0 1.3.2 2.5.6 3.6.1.3 0 .7-.2 1z"/></svg>(406) 555-0148</span>
        <span><svg width="10" height="10" viewBox="0 0 24 24"><path fill="#fff" d="M6 2h9v5H6zM4 8h16v12H4zm3 3v2h2v-2zm4 0v2h2v-2zm4 0v2h2v-2zm-8 4v2h2v-2zm4 0v2h2v-2zm4 0v2h2v-2z"/></svg>(406) 555-0192</span>
      </div>
    </div>
    <div class="brand-name brand-name--small"><span class="brand-name__square"></span>Crestline Decor Depot</div>
    <div class="footer-bar">
      <span><svg width="9" height="12" viewBox="0 0 12 16"><path fill="#fff" d="M6 0a6 6 0 0 0-6 6c0 4.5 6 10 6 10s6-5.5 6-10a6 6 0 0 0-6-6zm0 8.5A2.5 2.5 0 1 1 6 3.5a2.5 2.5 0 0 1 0 5z"/></svg>4823 Larkfield Drive Bozeman, MT 59744</span>
      <span><svg width="12" height="9" viewBox="0 0 16 12"><path fill="#fff" d="M0 0h16v1.5L8 6.5 0 1.5zM0 3.3l8 5 8-5V12H0z"/></svg>corinne@crestlinedecordepot.example</span>
      <span><svg width="11" height="11" viewBox="0 0 16 16"><circle cx="8" cy="8" r="7" fill="none" stroke="#fff" stroke-width="1.6"/><path d="M1 8h14M8 1c-3 4-3 10 0 14M8 1c3 4 3 10 0 14" fill="none" stroke="#fff" stroke-width="1.3"/></svg>www.crestlinedecordepot.example</span>
    </div>
  </section>

  <h2 class="side-label side-label--back">BACK SIDEE</h2>
  <section class="envelope envelope--back">
    <svg class="envelope__flap" width="1019" height="100" viewBox="0 0 1019 100">
      <polygon points="0,2 1019,2 965,97 54,97" fill="rgba(0,0,0,.25)"/>
      <polygon points="0,0 1019,0 963,94 53,94" fill="var(--brand-blue)"/>
    </svg>
    <div class="brand-name brand-name--large"><span class="brand-name__square"></span>Crestline Decor Depot</div>
  </section>
</body>
</html>
```